Brightway Dwelling & Yard Care - Maintenance & Improvements

Handyman service - Total home improvement and maintenance

We do everything indoors, ie. carpentry, and outdoors, ie. garden maintenance

No job too small or too unusual

7 Days per week
Updates

I want the overall impression not to favour either gender ... eg. maybe don't use the word Handy'man' because we also have a Fixmistress service .... but just stay with a generic theme of home improvement and maintenance

Industry/Entity Type

Home Improvement

Contact Information for Business Card

Brightway Dwelling & Yard Care
7 Days per Week
Total Home Maintenance and Improvements
Handyman | Fixmistress | Our (DIY) Task Pal
Ph: 0487 613 902
www.brightwaydwellingyard.com.au

Requirements
Must have
• The black and white image of various workers, as per attached

```html
<!DOCTYPE html>
<html lang="en">
<head>
<meta charset="utf-8">
<title>Brightway Dwelling &amp; Yard Care – Business Card</title>
<link rel="stylesheet" href="https://fonts.googleapis.com/css2?family=Arvo:wght@700&display=swap">
<style>
  :root {
    --leaf-green: #8aa63c;
    --ink: #2a2a2a;
    --paper: #ffffff;
    --backdrop: #eceeed;
  }
  * { margin: 0; padding: 0; box-sizing: border-box; }
  html, body {
    width: 1200px;
    height: 864px;
    overflow: hidden;
    background: var(--backdrop);
    font-family: "Arvo", Georgia, serif;
    font-weight: 700;
  }
  .business-card {
    position: absolute;
    left: 101px;
    top: 129px;
    width: 987px;
    height: 608px;
    background: var(--paper);
    overflow: hidden;
  }
  .brand-name {
    position: absolute;
    left: 38px;
    top: 0;
    color: var(--leaf-green);
    white-space: nowrap;
    font-weight: 700;
  }
  .brand-name-first {
    position: absolute;
    left: 0;
    top: 64px;
    font-size: 38px;
    line-height: 1;
  }
  .brand-name-second {
    position: absolute;
    left: 0;
    top: 140px;
    font-size: 52px;
    line-height: 1;
  }
  .trade-figures {
    position: absolute;
    left: 286px;
    top: 42px;
    width: 672px;
    height: 86px;
    background: linear-gradient(90deg, #9bb556, var(--leaf-green));
    opacity: 0.85;
  }
  .brand-rule {
    position: absolute;
    left: 676px;
    top: 175px;
    width: 284px;
    height: 3px;
    background: var(--leaf-green);
  }
  .contact {
    position: absolute;
    left: -17px;
    width: 100%;
    text-align: center;
    color: var(--ink);
    line-height: 1;
    white-space: nowrap;
  }
  .contact-phone {
    top: 258px;
    font-size: 37px;
    letter-spacing: 1px;
    display: flex;
    justify-content: center;
    align-items: center;
    gap: 10px;
  }
  .contact-phone svg { width: 32px; height: 40px; fill: var(--ink); }
  .contact-email { top: 340px; font-size: 23px; }
  .contact-web { top: 386px; font-size: 23px; }
  .service-band {
    position: absolute;
    left: 0;
    top: 435px;
    width: 100%;
    height: 173px;
    background: var(--leaf-green);
    color: var(--paper);
    text-align: center;
  }
  .service-line {
    position: absolute;
    left: 10px;
    width: 100%;
    line-height: 1;
    white-space: nowrap;
  }
  .service-summary { top: 24px; font-size: 40px; }
  .service-hours { top: 88px; font-size: 37px; }
</style>
</head>
<body>
  <section class="business-card">
    <h1 class="brand-name">
      <span class="brand-name-first">Brightway</span>
      <span class="brand-name-second">Dwelling &amp; Yard Care</span>
    </h1>
    <div class="trade-figures" role="img" aria-label="Row of green pictogram workers: plumber, mower, gardener with spade, wheelbarrow, carpenter, mechanic, painter with roller, worker on ladder"></div>
    <div class="brand-rule"></div>

    <p class="contact contact-phone">
      <svg viewBox="0 0 24 30" aria-hidden="true"><path d="M6 1c1.5-.6 2.6.2 3.2 1.6l1.6 4.2c.5 1.3.1 2.3-1 3l-1.6 1c-.5.4-.6 1-.3 1.7 1.2 3 2.5 5.4 4.3 7.6.5.6 1.1.7 1.6.3l1.5-1.1c1-.8 2.1-.7 3 .3l2.9 3.4c1 1.2.8 2.5-.3 3.4l-1.6 1.3c-1.6 1.3-3.7 1.5-5.6.1C7.5 24.5 3.4 17.6 2 10.3 1.5 7.5 2.4 3.6 4.3 2z"/></svg>
      <span>0487 613 902</span>
    </p>
    <p class="contact contact-email">help@brightwaydwellingyard.com.au</p>
    <p class="contact contact-web">www.brightwaydwellingyard.com.au</p>

    <div class="service-band">
      <p class="service-line service-summary">Total home improvement and maintenance</p>
      <p class="service-line service-hours">7 Days per week</p>
    </div>
  </section>
</body>
</html>
```